Stridewell Clinic (Podiatry and Physiotherapy) Clinical Brochure

You are producing a brochure that will sit in clinical/medical waiting rooms for our business Stridewell Clinic. A clinic that providers podiatry and physiotherapy services.

As you can see on our website www.stridewellclinic.example.nz we provide 6 different brands/services:
- Brightmoor Solutions
- Kestrelbay Solutions
- Varden Solutions
- Tolverstone Rehabilitation
- Ashgrove Solutions
- Merriwether Solutions

People will generally have found us through an ad e.g. search fungal nail treatment and end up straight on www.brightmoorsolutions.example.nz and therefore, each of the brands should be seen as being separate entities although part of the bigger brand Stridewell Clinic.

We are looking at a brochure (open to bi-fold, tri-fold etc.) that highlights all of our brands as well as the services that each of our brands provide which can be found on each of the websites listed above. We want this to be professional and informative yet simple and easy to read - this interpretation can be somewhat left up to you. This brochure will sit in waiting rooms/clinical environments.

I have attached our brand strategy so that you can understand our fonts and colours. I have also attached our logos for reference.

```html
<!DOCTYPE html>
<html lang="en">
<head>
<meta charset="utf-8">
<title>Stridewell Clinic – Clinical Brochure</title>
<link href="https://fonts.googleapis.com/css2?family=Bitter:wght@800&family=Montserrat:wght@400;500;700;800&display=swap" rel="stylesheet">
<style>
  :root{
    --blue:#1c5cbf;
    --blue-soft:#3f7bd2;
    --blue-deep:#154a9e;
    --navy:#101c33;
    --ink:#2b2b2b;
    --grey:#5d6470;
    --paper:#ffffff;
    --backdrop:#e4e5e7;
    --skin:#e9c3ad;
    --glove:#6fa9dd;
  }
  *{box-sizing:border-box;margin:0;padding:0}
  html,body{width:857px;height:1200px;overflow:hidden}
  body{background:var(--backdrop);font-family:"Montserrat",sans-serif;color:var(--ink);position:relative}

  .spread{position:absolute;left:38px;width:780px;height:552px;display:flex;box-shadow:0 10px 30px rgba(0,0,0,.18)}
  .spread--cover{top:34px}
  .spread--inside{top:620px}
  .page{position:relative;width:390px;height:552px;overflow:hidden;background:var(--paper)}
  .page + .page{border-left:1px solid rgba(0,0,0,.08)}

  .photo{position:absolute;border-radius:0}
  .photo--skin{background:linear-gradient(135deg,#f1d6c6,var(--skin) 55%,#c98f7a)}
  .photo--glove{background:linear-gradient(135deg,#f3e1d6,var(--glove) 60%,#4c86c4)}
  .photo--laser{background:linear-gradient(135deg,#f0dcd2,#d1304a 60%,#7a1a2a)}
  .photo--brace{background:linear-gradient(135deg,#eef1f4,#b9c2cc 50%,#2a2f38)}
  .photo--room{background:linear-gradient(135deg,#d9e4ec,#8ea8bc 55%,#3b4c5c)}
  .photo--family{background:linear-gradient(135deg,#e6dccf,#b58f76 50%,#4d5f76)}
  .photo--mono{background:linear-gradient(135deg,#f2f2f2,#bdbdbd 60%,#e4b0b0)}

  /* back cover */
  .back{background:var(--blue)}
  .back__panel{position:absolute;background:var(--blue-soft);border-radius:32px}
  .back__panel--dark{background:var(--blue-deep)}
  .back__tile{position:absolute;border-radius:26px;border:6px solid var(--paper)}
  .back__url{position:absolute;left:0;top:470px;width:272px;height:32px;background:var(--navy);color:var(--paper);font-size:10.5px;font-weight:500;letter-spacing:.3px;padding:9px 0 0 30px}

  /* front cover */
  .brand{position:absolute;left:120px;top:48px}
  .brand__name{font-weight:800;font-size:38px;line-height:1;color:var(--blue);letter-spacing:-1px}
  .brand__sub{margin-top:8px;font-size:15px;font-weight:500;color:var(--grey);letter-spacing:.4px}
  .hero__block{position:absolute;left:110px;top:170px;width:200px;height:350px;background:var(--blue)}
  .hero__photo{left:40px;top:222px;width:350px;height:240px}
  .hero__quote{position:absolute;left:40px;top:222px;width:250px;height:220px;background:rgba(28,92,191,.85);color:var(--paper);font-family:"Bitter",serif;font-weight:800;font-size:19px;line-height:1.3;padding:26px 22px}

  /* inside */
  .service{position:absolute;left:0;width:390px;height:170px}
  .service__photo{top:0;height:170px;width:170px}
  .service--photo-left .service__photo{left:0}
  .service--photo-right .service__photo{right:0}
  .service__copy{position:absolute;top:16px;width:196px}
  .service--photo-left .service__copy{left:186px}
  .service--photo-right .service__copy{left:18px}
  .service__label{background:var(--blue);color:var(--paper);font-family:"Bitter",serif;font-weight:800;font-size:17px;line-height:1.15;padding:12px 16px;box-shadow:-6px -6px 0 var(--navy);margin-left:6px}
  .service__text{margin-top:12px;font-size:8.5px;line-height:1.45;color:var(--grey);padding-left:6px}
</style>
</head>
<body>

<section class="spread spread--cover">
  <div class="page back">
    <div class="back__panel" style="left:200px;top:18px;width:180px;height:170px"></div>
    <div class="back__panel" style="left:20px;top:186px;width:190px;height:190px"></div>
    <div class="back__panel back__panel--dark" style="left:230px;top:390px;width:190px;height:190px"></div>
    <div class="back__tile photo--laser" role="img" aria-label="Foot resting on a red laser treatment device" style="left:64px;top:60px;width:150px;height:118px"></div>
    <div class="back__tile photo--glove" role="img" aria-label="Gloved hand examining a toenail" style="left:230px;top:96px;width:134px;height:112px"></div>
    <div class="back__tile photo--brace" role="img" aria-label="Ankle wrapped in a black support brace" style="left:44px;top:196px;width:150px;height:112px"></div>
    <div class="back__tile photo--glove" role="img" aria-label="Blue-gloved hands padding a toe" style="left:200px;top:222px;width:166px;height:136px"></div>
    <div class="back__url">www.stridewellclinic.example.nz</div>
  </div>

  <div class="page front">
    <div class="brand">
      <div class="brand__name">Stridewell<br>Clinic.</div>
      <div class="brand__sub">Ashgrove Solutions</div>
    </div>
    <div class="hero__block"></div>
    <div class="photo hero__photo photo--family" role="img" aria-label="Smiling family of three generations at home"></div>
    <div class="hero__quote">Your feet carry you through life, so make sure you've got the right foundations.</div>
  </div>
</section>

<section class="spread spread--inside">
  <div class="page">
    <div class="service service--photo-left" style="top:16px">
      <div class="photo service__photo photo--glove" role="img" aria-label="Gloved hands treating a toe"></div>
      <div class="service__copy">
        <div class="service__label">Brightmoor<br>Solutions</div>
        <p class="service__text">We are your experts in fungal nail health with the most comprehensive treatment programmes available, including the Glowline cold laser.</p>
      </div>
    </div>
    <div class="service service--photo-right" style="top:196px">
      <div class="photo service__photo photo--laser" role="img" aria-label="Foot under a red laser treatment device"></div>
      <div class="service__copy">
        <div class="service__label">Kestrelbay<br>Solutions</div>
        <p class="service__text">We are your experts in ingrown toenail care, offering gentle, lasting treatment under local anaesthetic for all ages.</p>
      </div>
    </div>
    <div class="service service--photo-left" style="top:370px">
      <div class="photo service__photo photo--mono" role="img" aria-label="Hands holding a sore heel"></div>
      <div class="service__copy">
        <div class="service__label">Varden<br>Solutions</div>
        <p class="service__text">Our highly trained and experienced podiatrists offer a range of treatments for heel pain, plantar fasciitis and related problems affecting people of all ages.</p>
      </div>
    </div>
  </div>

  <div class="page">
    <div class="service service--photo-right" style="top:16px">
      <div class="photo service__photo photo--brace" role="img" aria-label="Ankle in a support brace during rehabilitation"></div>
      <div class="service__copy">
        <div class="service__label">Tolverstone<br>Rehabilitation</div>
        <p class="service__text">Our highly trained and experienced team of physiotherapists and podiatrists offer a range of management strategies for foot, ankle, and leg problems affecting people of all ages and lifestyles.</p>
      </div>
    </div>
    <div class="service service--photo-left" style="top:196px">
      <div class="photo service__photo photo--glove" role="img" aria-label="Purple-gloved hand holding a foot with painted toenails"></div>
      <div class="service__copy">
        <div class="service__label">Ashgrove<br>Solutions</div>
        <p class="service__text">We are your experts in nail health with the most comprehensive treatment programmes available, including the Glowline cold laser.</p>
      </div>
    </div>
    <div class="service service--photo-right" style="top:370px">
      <div class="photo service__photo photo--room" role="img" aria-label="Bright clinic consultation room with a desk and laptop"></div>
      <div class="service__copy">
        <div class="service__label">Merriwether<br>Solutions</div>
        <p class="service__text">We are your experts in foot health with the most comprehensive treatment protocols available for all of your foot needs.</p>
      </div>
    </div>
  </div>
</section>

</body>
</html>
```